Marlowbrook Gin Label

Marlowbrook is an area of Liverpool. We have no desire for those who are aware of the area to associate it with football. We have a copy of Ketterdale Gin which is our brand attached to the files. Please can you read this and replicate but in red. Thanks.

```html
<!DOCTYPE html>
<html lang="en">
<head>
<meta charset="utf-8">
<title>Marlowbrook Gin Label</title>
<link href="https://fonts.googleapis.com/css2?family=Oswald:wght@500;600&family=Playfair+Display:ital,wght@1,700;1,900&family=Cinzel:wght@700&family=Sancreek&family=Libre+Baskerville:ital@0;1&display=swap" rel="stylesheet">
<style>
  :root {
    --bg: #000000;
    --red-deep: #8c2530;
    --red-mid: #b83540;
    --red-bright: #e64d57;
    --gold: #dcb84c;
    --gold-light: #f0d66a;
    --gold-box-a: #c29a22;
    --gold-box-b: #e5c64e;
    --ink: #141010;
    --script: #7a1a1f;
    --cream: #f4f1ee;
    --silver: #d6d2d2;
  }
  html, body {
    margin: 0;
    width: 1200px;
    height: 1200px;
    overflow: hidden;
    background: var(--bg);
  }
  .artboard { display: block; width: 1200px; height: 1200px; }
  .band-name { font-family: "Oswald", sans-serif; font-weight: 600; fill: var(--gold-light); }
  .band-tag { font-family: "Playfair Display", serif; font-style: italic; font-weight: 900; fill: var(--gold); letter-spacing: 2px; }
  .band-place { font-family: "Oswald", sans-serif; font-weight: 500; fill: var(--gold); }
  .seal-text { font-family: "Cinzel", serif; font-weight: 700; fill: var(--gold); letter-spacing: 3px; }
  .spec-label { font-family: "Oswald", sans-serif; font-weight: 600; fill: var(--ink); font-size: 21px; }
  .spec-value { font-family: "Libre Baskerville", serif; font-style: italic; fill: var(--ink); }
  .spec-hand { font-family: "Libre Baskerville", serif; font-style: italic; fill: var(--script); font-size: 19px; }
  .origin { font-family: "Cinzel", serif; font-weight: 700; fill: var(--gold); font-size: 20px; letter-spacing: 5px; }
  .brand-name { font-family: "Sancreek", serif; fill: var(--ink); stroke: var(--gold); stroke-width: 1.2px; paint-order: stroke; }
  .brand-gin { font-family: "Sancreek", serif; fill: var(--cream); }
  .claim { font-family: "Playfair Display", serif; font-style: italic; font-weight: 900; fill: var(--silver); letter-spacing: 4px; }
</style>
</head>
<body>
<svg class="artboard" viewBox="0 0 1200 1200" xmlns="http://www.w3.org/2000/svg">
  <defs>
    <linearGradient id="redSheen" x1="0" y1="0" x2="1" y2="0">
      <stop offset="0" stop-color="var(--red-deep)"/>
      <stop offset="0.55" stop-color="var(--red-mid)"/>
      <stop offset="1" stop-color="var(--red-bright)"/>
    </linearGradient>
    <linearGradient id="goldPlate" x1="0" y1="0" x2="1" y2="1">
      <stop offset="0" stop-color="var(--gold-box-b)"/>
      <stop offset="0.5" stop-color="var(--gold-box-a)"/>
      <stop offset="1" stop-color="var(--gold-box-b)"/>
    </linearGradient>
    <linearGradient id="engravingTone" x1="0" y1="0" x2="0" y2="1">
      <stop offset="0" stop-color="#5a1a20" stop-opacity="0.55"/>
      <stop offset="1" stop-color="#2a0c10" stop-opacity="0.75"/>
    </linearGradient>
    <pattern id="teethLeftDeep" width="8" height="10" patternUnits="userSpaceOnUse">
      <path d="M8 0 L0 5 L8 10 Z" fill="var(--red-deep)"/>
    </pattern>
    <pattern id="teethRightBright" width="8" height="10" patternUnits="userSpaceOnUse">
      <path d="M0 0 L8 5 L0 10 Z" fill="var(--red-bright)"/>
    </pattern>
    <path id="sealTopBand" d="M536 222 A70 70 0 0 1 676 222"/>
    <path id="sealBottomBand" d="M530 222 A76 76 0 0 0 682 222"/>
    <path id="sealTopLabel" d="M770 480 A55 55 0 0 1 880 480"/>
    <path id="sealBottomLabel" d="M764 480 A61 61 0 0 0 886 480"/>
  </defs>

  <!-- Neck band -->
  <g class="neck-band">
    <rect x="151" y="154" width="899" height="136" fill="url(#redSheen)"/>
    <rect x="143" y="155" width="8" height="134" fill="url(#teethLeftDeep)"/>
    <rect x="1050" y="155" width="8" height="134" fill="url(#teethRightBright)"/>
    <circle cx="606" cy="222" r="124" fill="url(#redSheen)"/>

    <g class="band-copy">
      <text class="band-name" x="222" y="211" font-size="52" textLength="208" lengthAdjust="spacingAndGlyphs">MARLOWBROOK</text>
      <text class="band-tag" x="217" y="240" font-size="19" textLength="218">HAND DISTILLED</text>
      <text class="band-place" x="220" y="272" font-size="22" textLength="217" lengthAdjust="spacingAndGlyphs">MERSEYSIDE, ENGLAND</text>
    </g>
    <g class="band-copy band-copy--flipped" transform="rotate(180 606 221)">
      <text class="band-name" x="222" y="211" font-size="52" textLength="208" lengthAdjust="spacingAndGlyphs">MARLOWBROOK</text>
      <text class="band-tag" x="217" y="240" font-size="19" textLength="218">HAND DISTILLED</text>
      <text class="band-place" x="220" y="272" font-size="22" textLength="217" lengthAdjust="spacingAndGlyphs">MERSEYSIDE, ENGLAND</text>
    </g>

    <g class="maker-seal">
      <circle cx="606" cy="222" r="98" fill="none" stroke="var(--gold)" stroke-width="3"/>
      <text class="seal-text" font-size="17"><textPath href="#sealTopBand" startOffset="50%" text-anchor="middle">THORNWICK</textPath></text>
      <text class="seal-text" font-size="14"><textPath href="#sealBottomBand" startOffset="50%" text-anchor="middle" dominant-baseline="hanging">SPIRITS CO.</textPath></text>
    </g>
  </g>

  <!-- Main label -->
  <g class="main-label">
    <rect x="230" y="386" width="737" height="708" fill="url(#redSheen)"/>
    <rect x="222" y="387" width="8" height="706" fill="url(#teethLeftDeep)"/>
    <rect x="967" y="387" width="8" height="706" fill="url(#teethRightBright)"/>

    <rect x="252" y="411" width="5" height="655" fill="var(--ink)"/>
    <rect x="942" y="411" width="5" height="655" fill="var(--ink)"/>

    <g class="spec-plate">
      <rect x="239" y="418" width="509" height="127" fill="url(#goldPlate)"/>
      <line x1="258" y1="429" x2="735" y2="429" stroke="var(--ink)" stroke-width="2"/>
      <line x1="258" y1="465" x2="715" y2="465" stroke="var(--ink)" stroke-width="1.2" stroke-dasharray="5 4"/>
      <line x1="258" y1="500" x2="715" y2="500" stroke="var(--ink)" stroke-width="1.2" stroke-dasharray="5 4"/>
      <line x1="258" y1="534" x2="735" y2="534" stroke="var(--ink)" stroke-width="2"/>
      <line x1="411" y1="438" x2="411" y2="460" stroke="var(--ink)" stroke-width="2"/>
      <line x1="571" y1="438" x2="571" y2="460" stroke="var(--ink)" stroke-width="2"/>
      <line x1="442" y1="473" x2="442" y2="495" stroke="var(--ink)" stroke-width="2"/>

      <text class="spec-label" x="278" y="457">BATCH</text>
      <text class="spec-value" x="453" y="457" font-size="21">40%<tspan font-size="15">VOL.</tspan></text>
      <text class="spec-value" x="618" y="457" font-size="21">70<tspan font-size="15">CL</tspan></text>
      <text class="spec-hand" x="275" y="493">Handcrafted</text>
      <text class="spec-label" x="454" y="492">BOTTLE</text>
      <text class="spec-label" x="298" y="527">DISTILLER</text>
      <text class="spec-hand" x="432" y="527">E. Holloway</text>
    </g>

    <g class="maker-seal">
      <circle cx="825" cy="480" r="80" fill="none" stroke="var(--gold)" stroke-width="3"/>
      <text class="seal-text" font-size="14"><textPath href="#sealTopLabel" startOffset="50%" text-anchor="middle">THORNWICK</textPath></text>
      <text class="seal-text" font-size="12"><textPath href="#sealBottomLabel" startOffset="50%" text-anchor="middle" dominant-baseline="hanging">SPIRITS CO.</textPath></text>
    </g>

    <text class="origin" x="601" y="600" text-anchor="middle" textLength="400">MERSEYSIDE, ENGLAND</text>

    <text class="brand-name" x="335" y="760" font-size="150" textLength="532" lengthAdjust="spacingAndGlyphs">MARLOWBROOK</text>
    <text class="brand-gin" x="621" y="884" font-size="150" textLength="199" lengthAdjust="spacingAndGlyphs" stroke="var(--red-deep)" stroke-width="1">GIN</text>

    <g role="img" aria-label="Engraved illustration of two Victorian gentlemen standing beside gin barrels">
      <rect x="298" y="786" width="236" height="270" rx="14" fill="url(#engravingTone)"/>
    </g>

    <g class="claims">
      <text class="claim" x="545" y="941" font-size="23" textLength="365">8 FINE BOTANICALS</text>
      <line x1="550" y1="952" x2="902" y2="952" stroke="var(--ink)" stroke-width="1.3" stroke-dasharray="5 4"/>
      <text class="claim" x="555" y="977" font-size="23" textLength="339">SMALL BATCH GIN</text>
      <line x1="550" y1="986" x2="902" y2="986" stroke="var(--ink)" stroke-width="1.3" stroke-dasharray="5 4"/>
      <text class="claim" x="585" y="1011" font-size="20" textLength="255">HAND DISTILLED</text>
      <line x1="550" y1="1020" x2="902" y2="1020" stroke="var(--ink)" stroke-width="1.3" stroke-dasharray="5 4"/>
    </g>
  </g>
</svg>
</body>
</html>
```